Brava Nest (Smart Home, Installation, Repair Industry) (Contest)

Looking for a website design for my company
Services we offer:
Phone Repair
TV Mounting
Security Camera Installation
Networking / Wi-Fi
Smart Home Services
IT Support

Looking for a website similar to trovely.example

Few tabs
About Us
Contact Us
Areas Served
Pricing and Services

```html
<!DOCTYPE html>
<html lang="en">
<head>
<meta charset="UTF-8">
<title>Brava Nest — Smart Home, Installation &amp; Repair</title>
<link href="https://fonts.googleapis.com/css2?family=Poppins:ital,wght@0,300;0,400;0,500;0,600;0,700;1,300;1,400&display=swap" rel="stylesheet">
<style>
:root{
  --orange:#f7941d;
  --orange-dark:#e5820c;
  --dark:#2a2a2a;
  --dark-2:#343434;
  --card:#3d3d3d;
  --ink:#222;
  --muted:#666;
  --light:#f2f2f2;
  --white:#fff;
  --blue:#1d6fe8;
  --cyan:#1ec3f2;
}
*{box-sizing:border-box;margin:0;padding:0}
html,body{width:1200px;height:3282px;overflow:hidden}
body{font-family:"Poppins",sans-serif;color:var(--ink);background:var(--white);position:relative}
section,header,footer{position:absolute;left:0;width:1200px}
.abs{position:absolute}
.btn{position:absolute;background:var(--orange);color:#fff;font-weight:700;font-size:12px;text-transform:uppercase;border-radius:4px;display:flex;align-items:center;justify-content:center;letter-spacing:.2px}
.brand{font-weight:700;font-size:28px;line-height:36px;color:var(--orange);letter-spacing:-.3px;white-space:nowrap}

/* hero */
.hero{top:0;height:489px;background:linear-gradient(100deg,#3d3d3d 0%,#4a4a47 45%,#5a5a52 70%,#45463f 100%)}
.hero-photo{position:absolute;left:300px;top:0;width:900px;height:489px;background:radial-gradient(ellipse at 60% 45%,rgba(120,110,95,.55),rgba(60,60,55,0) 65%)}
.nav{position:absolute;font-size:12px;color:#fff;font-weight:500}
.nav a{color:#fff;text-decoration:none;position:absolute;white-space:nowrap}
.nav a.active{color:var(--orange)}
.phone{position:absolute;left:897px;top:57px;width:154px;height:27px;border:1.5px solid #fff;border-radius:14px;color:#fff;font-size:12.5px;font-weight:500;display:flex;align-items:center;gap:6px;padding-left:9px}
.hero h1{position:absolute;left:149px;top:230px;color:#fff;font-size:27px;line-height:33px;font-weight:700;text-transform:uppercase}
.dots{position:absolute;top:472px;left:568px;display:flex;gap:4px}
.dots span{width:19px;height:3px;background:#fff;opacity:.8}

/* about */
.about{top:489px;height:363px;background:linear-gradient(90deg,#fff 55%,#f1f1f1 100%)}
.about h2{position:absolute;left:149px;top:60px;font-size:27px;font-weight:500}
.about h2 b{color:var(--orange);font-weight:700}
.about p{position:absolute;left:149px;width:422px;font-size:10.4px;line-height:19.5px;color:var(--muted);text-align:justify}
.about .img-a{left:683px;top:42px;width:226px;height:243px;background:linear-gradient(135deg,#f7a135,#e88a12)}
.about .img-b{left:803px;top:79px;width:248px;height:243px;background:radial-gradient(circle at 50% 45%,#1f8fa8,#0c4a66 60%,#082f45)}

/* success */
.success{top:852px;height:329px;background:var(--dark)}
.sec-title{position:absolute;left:0;width:1200px;text-align:center;font-size:26px;font-weight:600}
.success .sec-title{color:#fff;top:48px}
.stat{position:absolute;top:102px;height:163px;background:var(--card);text-align:center;color:#fff}
.stat svg{margin-top:32px}
.stat .num{font-size:34px;font-weight:600;color:var(--orange);line-height:40px;margin-top:6px}
.stat .lbl{font-size:14px;font-weight:400}

/* services */
.services{top:1181px;height:629px;background:#fff}
.services .sec-title{top:40px;color:#2c2c2c}
.svc{position:absolute;width:293px;height:222px;background:#fff;box-shadow:0 1px 4px rgba(0,0,0,.18)}
.svc .ph{height:185px}
.svc .bar{height:37px;display:flex;align-items:center;justify-content:space-between;padding-left:15px;font-size:14.5px;font-weight:600;color:#222}
.svc .go{width:34px;height:37px;background:var(--orange);display:flex;align-items:center;justify-content:center}

/* simple */
.simple{top:1810px;height:268px;background:#fff;border-top:1px solid #e6e6e6;border-bottom:1px solid #e6e6e6}
.simple h2{position:absolute;left:150px;top:36px;font-size:28px;line-height:33px;font-weight:600;color:#222}
.simple p{position:absolute;left:150px;top:112px;width:352px;font-size:10.4px;line-height:16.5px;color:var(--muted)}
.simple .ph{position:absolute;left:576px;top:0;width:624px;height:268px;background:linear-gradient(120deg,#dfe3e8,#c9b9a8 45%,#b2a393 70%,#e6e8ea)}

/* areas */
.areas{top:2078px;height:331px;background:#fff}
.areas h2{position:absolute;left:149px;top:95px;font-size:28px;font-weight:500;color:#2a2a2a}
.place{position:absolute;font-size:14.5px;color:#333;padding-left:19px}
.place small{display:block;font-size:10px;color:var(--orange);line-height:10px}
.place svg{position:absolute;left:0;top:4px}
.price-card{position:absolute;left:646px;top:88px;width:403px;height:206px}
.price-row{position:absolute;left:699px;width:290px;font-size:10.4px;color:#fff;display:flex;white-space:nowrap}
.price-row .fill{flex:1;border-bottom:1px dashed rgba(255,255,255,.85);margin:0 3px 4px}

/* feedback */
.feedback{top:2409px;height:380px;background:#2d2d2d}
.feedback .sec-title{top:40px;color:#fff}
.quote{position:absolute;left:583px;top:94px;width:32px;height:32px;border:2px solid #fff;border-radius:50%;color:#fff;font-size:20px;font-weight:700;text-align:center;line-height:34px}
.feedback p{position:absolute;left:250px;top:145px;width:700px;text-align:center;color:#aaa;font-size:10.6px;line-height:19.5px;font-style:italic}
.by{position:absolute;left:0;width:1200px;text-align:center;color:#bbb;font-size:10px}

/* partners */
.partners{top:2789px;height:205px;background:#fff}
.badge{position:absolute;top:63px;width:124px;height:92px;border:1px solid #e4e4e4;display:flex;align-items:center;justify-content:center}
.badge span{width:62px;height:62px;border-radius:50%;background:#5a5a5a}

/* footer */
.footer{top:2994px;height:288px;background:#2b2b2b;color:#cfcfcf}
.footer h4{position:absolute;top:38px;font-size:13px;font-weight:600;color:#eee}
.footer .brand{position:absolute;left:149px;top:52px}
.footer .blurb{position:absolute;left:149px;top:98px;width:225px;font-size:10.4px;line-height:18px;color:#bbb}
.social{position:absolute;left:150px;top:184px;display:flex;gap:7px}
.social span{width:23px;height:23px;border:1.5px solid #ddd;border-radius:50%}
.links{position:absolute;left:424px;top:72px;font-size:10.4px;line-height:21px;color:#bbb}
.news{position:absolute;left:592px;width:190px;font-size:10.4px;line-height:14px;color:#bbb}
.news .thumb{position:absolute;left:0;top:2px;width:45px;height:40px;background:linear-gradient(135deg,#e6e6e6,#9aa3ad)}
.news div{margin-left:58px}
.news em{color:var(--orange);font-style:normal}
.field{position:absolute;left:845px;width:206px;background:#3a3a3a;border:1px solid #444;font-size:9px;color:#ccc;padding:8px 7px}
.send{position:absolute;left:845px;top:198px;width:206px;height:26px;background:var(--orange);color:#fff;font-size:11.5px;font-weight:600;display:flex;align-items:center;justify-content:center}
.copy{position:absolute;left:0;top:261px;width:1200px;height:27px;background:#222;text-align:center;font-size:8.5px;line-height:27px;color:#ddd;text-transform:uppercase}
</style>
</head>
<body>

<header class="hero">
  <div class="hero-photo" role="img" aria-label="Smiling technician in a hard hat holding a security camera beside a ladder"></div>
  <div class="brand abs" style="left:149px;top:50px;">Brava Nest</div>
  <nav class="nav" style="left:0;top:0;width:1200px;">
    <a class="active" style="left:346px;top:63px;">HOME</a>
    <svg class="abs" style="left:360px;top:80px" width="8" height="6"><path d="M0 6 4 0 8 6z" fill="#f7941d"/></svg>
    <a style="left:412px;top:63px;">ABOUT US</a>
    <a style="left:502px;top:63px;">SERVICES</a>
    <a style="left:588px;top:63px;">PRICING</a>
    <a style="left:668px;top:63px;">AREAS SERVED</a>
    <a style="left:782px;top:63px;">CONTACT US</a>
  </nav>
  <div class="phone">
    <svg width="15" height="15" viewBox="0 0 16 16"><circle cx="8" cy="8" r="8" fill="#fff"/><path d="M5 4c.6-.4 1.1-.3 1.4.3l.6 1.3c.2.5 0 .8-.4 1.1.5 1.1 1.3 1.9 2.4 2.4.3-.4.6-.6 1.1-.4l1.3.6c.6.3.7.8.3 1.4-.7 1-2 1.3-3.2.6C6.4 10.3 5.2 9 4.4 7.1 3.9 5.9 4.1 4.7 5 4z" fill="#3d3d3d"/></svg>
    (800) 555 0142
  </div>
  <h1>Take control of<br>your home security</h1>
  <div class="btn" style="left:149px;top:310px;width:130px;height:35px;">Book a service</div>
  <div class="dots"><span></span><span style="opacity:.5"></span><span></span></div>
</header>

<section class="about">
  <h2>About <b>Brava Nest</b></h2>
  <p style="top:104px;">Lorem Ipsum is simply dummy text of the printing and typesetting industry. Lorem Ipsum has been the industry's standard dummy text ever since the 1500s, when an unknown printer took a galley of type and scrambled it to make a type specimen book. It has survived not only five centuries, but also the leap into electronic typesetting, remaining essentially unchanged.</p>
  <p style="top:222px;">It was popularised in the 1960s with the release of Lettrex sheets containing Lorem Ipsum passages, and more recently with desktop publishing software like Pagewright including versions of Lorem Ipsum.</p>
  <div class="abs img-a" role="img" aria-label="Close-up of a laptop keyboard in orange tone"></div>
  <div class="abs img-b" role="img" aria-label="Illustration of connected smart home devices on a circuit backdrop"></div>
</section>

<section class="success">
  <div class="sec-title">Our Some Success</div>
  <div class="stat" style="left:149px;width:218px;">
    <svg width="36" height="36" viewBox="0 0 36 36" fill="none" stroke="#fff" stroke-width="2"><path d="M10 4h16v10a8 8 0 0 1-16 0z"/><path d="M10 7H5v3a5 5 0 0 0 5 5M26 7h5v3a5 5 0 0 1-5 5M18 22v6M12 32h12"/><path d="M18 8l1.5 3 3 .4-2.2 2 .6 3-2.9-1.5-2.9 1.5.6-3-2.2-2 3-.4z" stroke-width="1.3"/></svg>
    <div class="num">150</div><div class="lbl">Awards Win</div>
  </div>
  <div class="stat" style="left:381px;width:218px;">
    <svg width="36" height="36" viewBox="0 0 36 36" fill="none" stroke="#fff" stroke-width="2"><circle cx="18" cy="18" r="15"/><circle cx="13" cy="14" r="1.3" fill="#fff"/><circle cx="23" cy="14" r="1.3" fill="#fff"/><path d="M11 21a8 8 0 0 0 14 0"/></svg>
    <div class="num">2500+</div><div class="lbl">Happy Clients</div>
  </div>
  <div class="stat" style="left:606px;width:217px;">
    <svg width="52" height="36" viewBox="0 0 52 36" fill="none" stroke="#fff" stroke-width="1.6"><circle cx="26" cy="8" r="4"/><path d="M19 20a7 7 0 0 1 14 0"/><path d="M26 22l2 4 4 .5-3 3 .8 4-3.8-2-3.8 2 .8-4-3-3 4-.5zM12 18l1.4 3 3 .4-2.2 2 .6 3-2.8-1.5-2.8 1.5.6-3-2.2-2 3-.4zM40 18l1.4 3 3 .4-2.2 2 .6 3-2.8-1.5-2.8 1.5.6-3-2.2-2 3-.4z"/></svg>
    <div class="num">7+</div><div class="lbl">Years Experience</div>
  </div>
  <div class="stat" style="left:833px;width:218px;">
    <svg width="40" height="36" viewBox="0 0 40 36" fill="none" stroke="#fff" stroke-width="2"><path d="M14 6h-4v26h24V6h-4"/><rect x="14" y="3" width="12" height="6" rx="1"/><path d="M15 20l4 4 8-9"/><path d="M3 30l6-6 5 4" stroke-width="1.6"/></svg>
    <div class="num">3000+</div><div class="lbl">Project Done</div>
  </div>
</section>

<section class="services">
  <div class="sec-title">Our Services</div>
  <div class="svc" style="left:150px;top:111px;">
    <div class="ph" role="img" aria-label="Hands repairing an opened smartphone with a screwdriver" style="background:linear-gradient(135deg,#d9b8a0,#5a6f86 55%,#1f2e45)"></div>
    <div class="bar">Phone Repair<span class="go"><svg width="14" height="12"><path d="M2 1l5 5-5 5M7 1l5 5-5 5" stroke="#fff" stroke-width="2" fill="none"/></svg></span></div>
  </div>
  <div class="svc" style="left:454px;top:111px;">
    <div class="ph" role="img" aria-label="Two installers mounting a flat screen TV on a wall" style="background:linear-gradient(180deg,#f4f4f4,#cfcfcf 40%,#3a3a3a 60%,#eee)"></div>
    <div class="bar">TV Mounting<span class="go"><svg width="14" height="12"><path d="M2 1l5 5-5 5M7 1l5 5-5 5" stroke="#fff" stroke-width="2" fill="none"/></svg></span></div>
  </div>
  <div class="svc" style="left:757px;top:111px;">
    <div class="ph" role="img" aria-label="Hand holding a white security camera" style="background:radial-gradient(circle at 60% 45%,#f7f7f7,#cfcfcf 50%,#8e8e8e)"></div>
    <div class="bar">Security Camera Installation<span class="go"><svg width="14" height="12"><path d="M2 1l5 5-5 5M7 1l5 5-5 5" stroke="#fff" stroke-width="2" fill="none"/></svg></span></div>
  </div>
  <div class="svc" style="left:150px;top:344px;">
    <div class="ph" role="img" aria-label="Hand plugging network cables into a switch" style="background:linear-gradient(180deg,#2b2b2b,#6b6b6b 45%,#d8c4b8)"></div>
    <div class="bar">Networking / Wi-Fi<span class="go"><svg width="14" height="12"><path d="M2 1l5 5-5 5M7 1l5 5-5 5" stroke="#fff" stroke-width="2" fill="none"/></svg></span></div>
  </div>
  <div class="svc" style="left:454px;top:344px;">
    <div class="ph" role="img" aria-label="Hand holding a phone running a smart home app in a living room" style="background:linear-gradient(135deg,#e0d8cc,#b8c4cc 50%,#7f8e99)"></div>
    <div class="bar">Smart Home Services<span class="go"><svg width="14" height="12"><path d="M2 1l5 5-5 5M7 1l5 5-5 5" stroke="#fff" stroke-width="2" fill="none"/></svg></span></div>
  </div>
  <div class="svc" style="left:757px;top:344px;">
    <div class="ph" role="img" aria-label="Hand typing on a white keyboard" style="background:linear-gradient(135deg,#eef3f6,#c9d3da 55%,#e8e2dc)"></div>
    <div class="bar">IT Support<span class="go"><svg width="14" height="12"><path d="M2 1l5 5-5 5M7 1l5 5-5 5" stroke="#fff" stroke-width="2" fill="none"/></svg></span></div>
  </div>
</section>

<section class="simple">
  <h2>A simple way to take care<br>of everything</h2>
  <p>Lorem Ipsum is simply dummy text of the printing and typesetting industry. Lorem Ipsum has been the industry's standard dummy text ever since the 1500s, when an unknown printer took a galley of type and scrambled it to make a type specimen book.</p>
  <div class="btn" style="left:151px;top:194px;width:130px;height:36px;">Book a service</div>
  <div class="ph" role="img" aria-label="Happy family relaxing together on a sofa looking at a phone"></div>
</section>

<section class="areas">
  <h2>Areas Served</h2>
  <div class="place" style="left:150px;top:153px;"><svg width="11" height="14" viewBox="0 0 11 14"><path d="M5.5 0A5.5 5.5 0 0 0 0 5.5C0 9.5 5.5 14 5.5 14S11 9.5 11 5.5A5.5 5.5 0 0 0 5.5 0z" fill="#333"/><circle cx="5.5" cy="5.5" r="2" fill="#fff"/></svg>Toronto<small>View map</small></div>
  <div class="place" style="left:255px;top:153px;"><svg width="11" height="14" viewBox="0 0 11 14"><path d="M5.5 0A5.5 5.5 0 0 0 0 5.5C0 9.5 5.5 14 5.5 14S11 9.5 11 5.5A5.5 5.5 0 0 0 5.5 0z" fill="#333"/><circle cx="5.5" cy="5.5" r="2" fill="#fff"/></svg>Toronto<small>View map</small></div>
  <div class="place" style="left:360px;top:153px;"><svg width="11" height="14" viewBox="0 0 11 14"><path d="M5.5 0A5.5 5.5 0 0 0 0 5.5C0 9.5 5.5 14 5.5 14S11 9.5 11 5.5A5.5 5.5 0 0 0 5.5 0z" fill="#333"/><circle cx="5.5" cy="5.5" r="2" fill="#fff"/></svg>Toronto<small>View map</small></div>
  <div class="place" style="left:150px;top:212px;"><svg width="11" height="14" viewBox="0 0 11 14"><path d="M5.5 0A5.5 5.5 0 0 0 0 5.5C0 9.5 5.5 14 5.5 14S11 9.5 11 5.5A5.5 5.5 0 0 0 5.5 0z" fill="#333"/><circle cx="5.5" cy="5.5" r="2" fill="#fff"/></svg>Toronto<small>View map</small></div>
  <div class="place" style="left:255px;top:212px;"><svg width="11" height="14" viewBox="0 0 11 14"><path d="M5.5 0A5.5 5.5 0 0 0 0 5.5C0 9.5 5.5 14 5.5 14S11 9.5 11 5.5A5.5 5.5 0 0 0 5.5 0z" fill="#333"/><circle cx="5.5" cy="5.5" r="2" fill="#fff"/></svg>Toronto<small>View map</small></div>
  <div class="place" style="left:360px;top:212px;"><svg width="11" height="14" viewBox="0 0 11 14"><path d="M5.5 0A5.5 5.5 0 0 0 0 5.5C0 9.5 5.5 14 5.5 14S11 9.5 11 5.5A5.5 5.5 0 0 0 5.5 0z" fill="#333"/><circle cx="5.5" cy="5.5" r="2" fill="#fff"/></svg>Toronto<small>View map</small></div>

  <svg class="price-card" viewBox="0 0 403 206">
    <defs><linearGradient id="pg" x1="0" x2="1"><stop offset="0" stop-color="#1a5ee6"/><stop offset="1" stop-color="#1ec5f3"/></linearGradient></defs>
    <ellipse cx="200" cy="200" rx="180" ry="6" fill="rgba(0,0,0,.08)"/>
    <path d="M10 20h383q12 0 9 12l-38 150q-3 16-20 16H60q-17 0-21-16L2 32q-3-12 8-12z" fill="url(#pg)"/>
    <path d="M46 0l-6 20h8zM354 0l6 20h-8z" fill="#0e47b5"/>
    <rect x="48" y="0" width="306" height="52" rx="4" fill="#f7941d"/>
    <text x="201" y="34" text-anchor="middle" fill="#fff" font-family="Poppins,sans-serif" font-weight="700" font-size="21">PRICING</text>
  </svg>
  <div class="price-row" style="top:139px;">Phone Repair<span class="fill"></span>$20.00</div>
  <div class="price-row" style="top:159px;">TV Mounting<span class="fill"></span>-$20.00</div>
  <div class="price-row" style="top:178px;">Security Camera Installation<span class="fill"></span>-$20.00</div>
  <div class="price-row" style="top:197px;">Networking / Wi-Fi<span class="fill"></span>-$20.00</div>
  <div class="price-row" style="top:217px;width:295px;">Smart Home Services<span class="fill"></span>$20.00</div>
  <div class="price-row" style="top:237px;width:295px;">IT Support<span class="fill"></span>$20.00</div>
</section>

<section class="feedback">
  <div class="sec-title">Client Feedback</div>
  <div class="quote">“</div>
  <p>Lorem Ipsum is simply dummy text of the printing and typesetting industry. Lorem Ipsum has been the industry's standard dummy text ever since the 1500s, when an unknown printer took a galley of type and scrambled it to make a type specimen book. standard dummy text ever since the 1500s, when an unknown printer took.</p>
  <div class="by" style="top:220px;">by</div>
  <div class="by" style="top:236px;color:#fff;font-weight:600;">MARCUS HALE</div>
  <svg class="abs" style="left:548px;top:262px" width="104" height="68" viewBox="0 0 104 68">
    <g fill="#8a8a8a" stroke="#fff" stroke-width="2">
      <path d="M18 2l15 8v17l-15 8-15-8V10z"/>
      <path d="M52 2l15 8v17l-15 8-15-8V10z" fill="#6f6f6f"/>
      <path d="M86 2l15 8v17l-15 8-15-8V10z"/>
      <path d="M35 32l15 8v17l-15 8-15-8V40z"/>
      <path d="M69 32l15 8v17l-15 8-15-8V40z"/>
    </g>
  </svg>
</section>

<section class="partners">
  <div class="badge" style="left:178px;"><span></span></div>
  <div class="badge" style="left:324px;"><span style="border-radius:0;width:50px;height:40px"></span></div>
  <div class="badge" style="left:470px;"><span></span></div>
  <div class="badge" style="left:617px;"><span style="border-radius:0;width:70px;height:18px"></span></div>
  <div class="badge" style="left:763px;"><span></span></div>
  <div class="badge" style="left:909px;"><span style="background:#bdbdbd"></span></div>
</section>

<footer class="footer">
  <div class="brand">Brava Nest</div>
  <div class="blurb">Lorem Ipsum is simply dummy text of the printing and typesetting industry. Lorem Ipsum has been the industry's standard dummy text ever since the 1500s</div>
  <div class="social"><span></span><span></span><span></span><span></span></div>

  <h4 style="left:422px;">QUICK LINKS</h4>
  <div class="links">Home<br>About Us<br>Services<br>Pricing<br>Areas Served<br>Contact Us</div>

  <h4 style="left:592px;">LATEST NEWS</h4>
  <div class="news" style="top:74px;"><span class="thumb" role="img" aria-label="News thumbnail"></span><div>Lorem Ipsum is simply dummy text of the<br><em>15 Dec, 2019</em></div></div>
  <div class="news" style="top:136px;"><span class="thumb" role="img" aria-label="News thumbnail" style="background:linear-gradient(135deg,#cfe7ea,#7fb6c0)"></span><div>Lorem Ipsum is simply dummy text of the<br><em>15 Dec, 2019</em></div></div>

  <h4 style="left:845px;">GET IN TOUCH</h4>
  <div class="field" style="top:72px;height:26px;">Name:</div>
  <div class="field" style="top:104px;height:26px;">Email:</div>
  <div class="field" style="top:136px;height:58px;">Email:</div>
  <div class="send">SEND</div>
  <div class="copy">© 2020 Brava Nest &nbsp;All rights reserved.</div>
</footer>

</body>
</html>
```